Brightfield Co Trade Show Flyer

We need a brochure design (8.5 x 11) Info in the design (refer to rough draft I drew on Paper): "#1 selling tool to aquire new franchisees has been video testimonials" - Martin L. Crowe, C.E.O Tovik Smoothie Franchise Testimonials - Let your franchisees do the selling for you. Franchisee testimonial: $10,000 / per Franchisee Includes: • 2 minute Video • 1 minute add for your franchise's location • Concept creation • Communication with franchisee • Travel to their location • All rental equipment • 1 round of corrections • Animated logo • Licensed music ******* For 25% Discount section (next to middle box), please put the "Outlet Summit Logo" Great to use on all your social media (USE logos and icons) • Website • YouTube • LinkedIn • Facebook • Instagram • Twitter • Phone calls • Emails • In person meetings Some of our clients: (use the logos I uploaded - in round boxes as in draft) LOGO (Brightfield Franchise Testimonial) www.brightfieldvoices.example (866) 555-0172

Target Market(s)

Franchise owners

Colors

Designer to choose colors to be used in the design.

Requirements

```html
<!DOCTYPE html>
<html lang="en">
<head>
<meta charset="utf-8">
<title>Brightfield Franchise Testimonials – Trade Show Flyer</title>
<link href="https://fonts.googleapis.com/css2?family=Montserrat:wght@800;900&family=Lato:ital,wght@0,400;0,700;0,900;1,400;1,700&family=Fira+Sans:ital,wght@1,500;1,800&family=Arimo:wght@700&display=swap" rel="stylesheet">
<style>
  :root {
    --mat: #747272;
    --paper: #ffffff;
    --brand-red: #ed1b3b;
    --ink: #4a4b4d;
    --ink-dark: #111111;
    --bubble-grey: #5b5c5e;
    --summit-teal: #13a88f;
    --band-top: #2a2829;
    --band-bottom: #3b393a;
  }
  html, body {
    margin: 0;
    padding: 0;
    width: 945px;
    height: 1200px;
    overflow: hidden;
    background: var(--mat);
  }
  .flyer { display: block; width: 945px; height: 1200px; }
  .quote-text { font-family: 'Lato', sans-serif; font-weight: 700; font-size: 17px; fill: var(--ink-dark); }
  .quote-author { font-family: 'Lato', sans-serif; font-weight: 700; font-style: italic; font-size: 17px; fill: var(--ink-dark); }
  .quote-role { font-family: 'Lato', sans-serif; font-weight: 400; font-style: italic; font-size: 16px; fill: var(--ink); }
  .headline { font-family: 'Montserrat', sans-serif; font-weight: 900; font-size: 82px; fill: var(--ink); }
  .pitch { font-family: 'Lato', sans-serif; font-weight: 900; font-size: 33px; fill: var(--brand-red); }
  .price { font-family: 'Fira Sans', sans-serif; font-style: italic; font-weight: 800; font-size: 33px; fill: var(--paper); }
  .price-sub { font-family: 'Fira Sans', sans-serif; font-style: italic; font-weight: 800; font-size: 21px; fill: var(--paper); }
  .perk { font-family: 'Fira Sans', sans-serif; font-style: italic; font-weight: 500; font-size: 17.5px; fill: var(--paper); }
  .tick { fill: none; stroke: var(--paper); stroke-width: 2.4; stroke-linecap: round; stroke-linejoin: round; }
  .discount-figure { font-family: 'Montserrat', sans-serif; font-weight: 900; font-size: 132px; fill: var(--paper); }
  .discount-percent { font-family: 'Montserrat', sans-serif; font-weight: 900; font-size: 84px; fill: var(--paper); }
  .discount-label { font-family: 'Montserrat', sans-serif; font-weight: 900; font-size: 30px; fill: var(--paper); }
  .partner-name { font-family: 'Montserrat', sans-serif; font-weight: 900; font-size: 20px; fill: var(--paper); }
  .brand-name { font-family: 'Montserrat', sans-serif; font-weight: 900; font-size: 44px; fill: var(--ink-dark); }
  .brand-tag { font-family: 'Arimo', sans-serif; font-weight: 700; font-size: 13px; fill: var(--ink-dark); }
  .trusted-label { font-family: 'Lato', sans-serif; font-weight: 400; font-size: 12px; fill: var(--ink); }
  .client-name { font-family: 'Lato', sans-serif; font-weight: 700; font-size: 10px; fill: var(--ink); }
  .web-address { font-family: 'Lato', sans-serif; font-weight: 700; font-size: 22px; fill: var(--brand-red); }
  .phone-number { font-family: 'Lato', sans-serif; font-weight: 900; font-size: 31px; fill: var(--ink-dark); }
  .band-title { font-family: 'Lato', sans-serif; font-weight: 900; font-size: 26px; fill: var(--paper); }
  .band-title .accent { fill: var(--brand-red); }
  .channel-disc { fill: var(--paper); }
  .channel-glyph { fill: none; stroke: var(--brand-red); stroke-width: 2.2; stroke-linecap: round; stroke-linejoin: round; }
</style>
</head>
<body>
<svg class="flyer" viewBox="0 0 945 1200" xmlns="http://www.w3.org/2000/svg">
  <defs>
    <linearGradient id="band-fade" x1="0" y1="0" x2="0" y2="1">
      <stop offset="0" stop-color="var(--band-top)"/>
      <stop offset="1" stop-color="var(--band-bottom)"/>
    </linearGradient>
  </defs>

  <!-- page -->
  <rect class="page" x="80" y="92" width="785" height="1016" fill="var(--paper)"/>

  <!-- testimonial quote -->
  <g class="quote-mark" fill="var(--brand-red)">
    <path d="M154,178 h22 a5,5 0 0 0 5,-5 v-22 a5,5 0 0 0 -5,-5 h-9 c0,-7 4,-11 11,-12 v-11 c-18,1 -32,12 -32,34 v16 a5,5 0 0 0 5,5 z"/>
    <path d="M189,178 h22 a5,5 0 0 0 5,-5 v-22 a5,5 0 0 0 -5,-5 h-9 c0,-7 4,-11 11,-12 v-11 c-18,1 -32,12 -32,34 v16 a5,5 0 0 0 5,5 z"/>
  </g>
  <text class="quote-text" x="236" y="152" textLength="560" lengthAdjust="spacingAndGlyphs">#1 selling tool to aquire new franchisees has been video testimonials”</text>
  <text x="803" y="176" text-anchor="end"><tspan class="quote-author">- Martin L. Crowe, </tspan><tspan class="quote-role">C.E.O Tovik Smoothie</tspan></text>

  <!-- headline -->
  <text class="headline" x="142" y="277" textLength="520" lengthAdjust="spacingAndGlyphs">FRANCHISE</text>
  <text class="headline" x="138" y="350" textLength="676" lengthAdjust="spacingAndGlyphs">TESTIMONIALS</text>

  <!-- pitch -->
  <g class="pitch">
    <text x="153" y="414">LET YOUR</text>
    <text x="153" y="449">FRANCHISEES</text>
    <text x="153" y="484">DO THE SELLING</text>
    <text x="153" y="519">FOR YOU.</text>
  </g>

  <!-- discount bubble -->
  <path class="discount-bubble" fill="var(--bubble-grey)"
        d="M169,547 H460 V813 a20,20 0 0 1 -20,20 H293 L222,883 a4,4 0 0 1 -7,-3 V833 H169 a20,20 0 0 1 -20,-20 V567 a20,20 0 0 1 20,-20 z"/>
  <text class="discount-figure" x="172" y="669" textLength="150" lengthAdjust="spacingAndGlyphs">25</text>
  <text class="discount-percent" x="330" y="668" textLength="84" lengthAdjust="spacingAndGlyphs">%</text>
  <text class="discount-label" x="177" y="708" textLength="181" lengthAdjust="spacingAndGlyphs">DISCOUNT</text>
  <text class="discount-label" x="177" y="741">FOR</text>
  <g class="partner-mark">
    <rect x="278" y="736" width="16" height="16" fill="var(--summit-teal)"/>
    <text class="partner-name" x="302" y="752">Outlet</text>
    <text class="partner-name" x="302" y="776">Summit</text>
  </g>

  <!-- package bubble -->
  <path class="package-bubble" fill="var(--brand-red)" stroke="var(--paper)" stroke-width="8" stroke-linejoin="round"
        d="M464,387 H762 a20,20 0 0 1 20,20 V669 a20,20 0 0 1 -20,20 H734 a10,10 0 0 0 -10,10 V741 a4,4 0 0 1 -6,3 L642,689 H464 a20,20 0 0 1 -20,-20 V407 a20,20 0 0 1 20,-20 z"/>
  <text class="price" x="477" y="426">$10,000 / per</text>
  <text class="price-sub" x="477" y="453">Franchisee Includes:</text>
  <g class="perks">
    <polyline class="tick" points="480,474 484,478 491,471"/>
    <text class="perk" x="500" y="480">2 minute Video</text>
    <polyline class="tick" points="480,496 484,500 491,493"/>
    <text class="perk" x="500" y="502">1 minute add for your</text>
    <text class="perk" x="500" y="523">franchise’s location</text>
    <polyline class="tick" points="480,539 484,543 491,536"/>
    <text class="perk" x="500" y="545">Concept creation</text>
    <polyline class="tick" points="480,560 484,564 491,557"/>
    <text class="perk" x="500" y="566">Communication with franchisee</text>
    <polyline class="tick" points="480,582 484,586 491,579"/>
    <text class="perk" x="500" y="588">Travel to their location</text>
    <polyline class="tick" points="480,603 484,607 491,600"/>
    <text class="perk" x="500" y="609">All rental equipment</text>
    <polyline class="tick" points="480,625 484,629 491,622"/>
    <text class="perk" x="500" y="631">1 round of corrections</text>
    <polyline class="tick" points="480,646 484,650 491,643"/>
    <text class="perk" x="500" y="652">Animated logo</text>
    <polyline class="tick" points="480,668 484,672 491,665"/>
    <text class="perk" x="500" y="674">Licensed music</text>
  </g>

  <!-- brand block -->
  <circle class="brand-disc" cx="641" cy="782" r="34" fill="var(--ink-dark)"/>
  <text class="brand-name" x="646" y="878" text-anchor="middle" textLength="262" lengthAdjust="spacingAndGlyphs">BRIGHTFIELD</text>
  <line x1="543" y1="892" x2="550" y2="892" stroke="var(--ink)" stroke-width="1"/>
  <text class="brand-tag" x="646" y="897" text-anchor="middle">FRANCHISE TESTIMONIALS</text>
  <line x1="741" y1="892" x2="748" y2="892" stroke="var(--ink)" stroke-width="1"/>

  <!-- contact -->
  <text class="web-address" x="652" y="930" text-anchor="middle" textLength="323" lengthAdjust="spacingAndGlyphs">www.brightfieldvoices.example</text>
  <rect x="508" y="942" width="33" height="32" rx="5" fill="var(--brand-red)"/>
  <path d="M517,950 l4,-1 3,6 -2,2 c1,3 3,5 6,6 l2,-2 6,3 -1,4 c-9,1 -18,-8 -18,-18 z" fill="var(--paper)"/>
  <text class="phone-number" x="548" y="969" textLength="238" lengthAdjust="spacingAndGlyphs">(866) 555-0172</text>

  <!-- clients -->
  <line x1="213" y1="913" x2="245" y2="913" stroke="var(--ink)" stroke-width="0.8"/>
  <text class="trusted-label" x="287" y="917" text-anchor="middle">TRUSTED BY</text>
  <line x1="327" y1="913" x2="359" y2="913" stroke="var(--ink)" stroke-width="0.8"/>
  <g class="clients">
    <text class="client-name" x="153" y="952" text-anchor="middle">Pinecrest</text>
    <text class="client-name" x="153" y="964" text-anchor="middle">Creamery</text>
    <text class="client-name" x="209" y="952" text-anchor="middle">Daybreak</text>
    <text class="client-name" x="209" y="964" text-anchor="middle">Mart</text>
    <text class="client-name" x="271" y="952" text-anchor="middle">Tovik</text>
    <text class="client-name" x="271" y="964" text-anchor="middle">Smoothie</text>
    <text class="client-name" x="338" y="952" text-anchor="middle">Clearline</text>
    <text class="client-name" x="338" y="964" text-anchor="middle">Cleaning</text>
    <text class="client-name" x="415" y="952" text-anchor="middle">Roadmark</text>
    <text class="client-name" x="415" y="964" text-anchor="middle">Auto</text>
  </g>

  <!-- channels band -->
  <path class="channel-band" fill="url(#band-fade)" d="M156,1010 H786 a22,22 0 0 1 22,22 V1108 H134 V1032 a22,22 0 0 1 22,-22 z"/>
  <text class="band-title" x="485" y="1046" text-anchor="middle">USE YOUR <tspan class="accent">TESTIMONIALS</tspan> EVERYWHERE</text>
  <g class="channels">
    <circle class="channel-disc" cx="285" cy="1073" r="17" aria-label="Website"/>
    <circle class="channel-glyph" cx="285" cy="1073" r="8"/>
    <path class="channel-glyph" d="M277,1073 h16 M285,1065 c-5,5 -5,11 0,16 c5,-5 5,-11 0,-16"/>
    <circle class="channel-disc" cx="341" cy="1073" r="17" aria-label="Video channel"/>
    <circle class="channel-disc" cx="397" cy="1073" r="17" aria-label="Professional network"/>
    <circle class="channel-disc" cx="450" cy="1073" r="17" aria-label="Social page"/>
    <circle class="channel-disc" cx="506" cy="1073" r="17" aria-label="Microblog"/>
    <circle class="channel-disc" cx="563" cy="1073" r="17" aria-label="Photo sharing"/>
    <circle class="channel-disc" cx="616" cy="1073" r="17" aria-label="Phone calls"/>
    <rect class="channel-glyph" x="611" y="1063" width="10" height="19" rx="2"/>
    <circle class="channel-disc" cx="672" cy="1073" r="17" aria-label="Email"/>
    <rect class="channel-glyph" x="663" y="1067" width="18" height="12" rx="1"/>
    <polyline class="channel-glyph" points="663,1067 672,1074 681,1067"/>
  </g>
</svg>
</body>
</html>
```